Design some Business Cards for my Business

Looking for design of a two sided business card with full color and bleed

SIDE ONE
Logo
Website Address

SIDE TWO
Name
Phone Number
Email

Information to go on the card is on the PSD file called Business Card

OTHER INFORMATION
- You can put the website address on either the front or back. You decide.
- You have room to make minor adjustments to the logo. As you can see I put a shadow on some of them to see what would look like. If you find something that you think I may like then try it. I am open to slight changes to give u an edge.

RM.

```html
<!DOCTYPE html>
<html lang="en">
<head>
<meta charset="utf-8">
<title>Northern Cards – Business Cards</title>
<link href="https://fonts.googleapis.com/css2?family=Open+Sans:wght@400;600;700&display=swap" rel="stylesheet">
<style>
  :root{
    --page:#e6e6e8;
    --card-white:#f4f3f3;
    --pattern-light:#e9e7e7;
    --red:#c8202f;
    --red-dark:#a3161f;
    --red-light:#d5303c;
    --ink:#ffffff;
    --divider:rgba(255,255,255,.35);
    --shadow:rgba(0,0,0,.25);
  }
  *{margin:0;padding:0;box-sizing:border-box}
  html,body{width:1200px;height:901px;overflow:hidden}
  body{background:var(--page);font-family:"Open Sans",Arial,sans-serif;position:relative}
  .card{position:absolute;width:560px;height:320px;border-radius:4px;overflow:hidden;box-shadow:0 10px 30px var(--shadow)}
  .card--front{left:320px;top:70px;background:var(--card-white)}
  .card--back{left:320px;top:490px;background:var(--red)}

  .front-pattern{position:absolute;inset:0;background:linear-gradient(135deg,var(--card-white),var(--pattern-light))}
  .front-band{position:absolute;left:0;top:0;width:100%;height:100%}
  .front-logo{position:absolute;left:0;right:0;top:52px;text-align:center}
  .wordmark{font-weight:700;font-size:44px;letter-spacing:.5px;color:var(--red)}
  .front-name{position:absolute;left:40px;top:232px;font-weight:700;font-size:24px;color:var(--ink)}
  .front-divider{position:absolute;left:250px;top:190px;width:1px;height:108px;background:var(--divider)}
  .contact-list{position:absolute;left:275px;top:200px;list-style:none;color:var(--ink);font-size:15px}
  .contact-list li{display:flex;align-items:center;gap:10px;height:30px}
  .contact-list svg{width:16px;height:16px;flex:none}

  .back-pattern{position:absolute;inset:0;background:radial-gradient(ellipse at 55% 45%,var(--red-light),var(--red) 55%,var(--red-dark))}
  .back-logo{position:absolute;left:0;right:0;top:118px;text-align:center}
  .back-logo .wordmark{color:var(--ink);font-size:50px}
  .back-web{position:absolute;left:40px;bottom:30px;color:var(--ink);font-size:15px;font-weight:400}
</style>
</head>
<body>
  <section class="card card--front" aria-label="Business card front">
    <div class="front-pattern" role="img" aria-label="Faint repeated brand-name pattern in light grey"></div>
    <svg class="front-band" viewBox="0 0 560 320" preserveAspectRatio="none" aria-hidden="true">
      <polygon points="0,186 560,168 560,320 0,320" fill="#c8202f"/>
      <polygon points="0,180 560,162 560,168 0,186" fill="#8f1219" opacity=".35"/>
    </svg>
    <div class="front-logo"><span class="wordmark">Northern Cards</span></div>
    <div class="front-name">RM.</div>
    <div class="front-divider"></div>
    <ul class="contact-list">
      <li>
        <svg viewBox="0 0 16 16" aria-hidden="true"><circle cx="8" cy="8" r="8" fill="#fff"/><path d="M5.5 4.5l1.3 0 .6 1.8-.8.6a5 5 0 0 0 2.5 2.5l.6-.8 1.8.6 0 1.3c0 .4-.4.8-.8.8A6.5 6.5 0 0 1 4.7 5.3c0-.4.4-.8.8-.8z" fill="#c8202f"/></svg>
        555 010 2233
      </li>
      <li>
        <svg viewBox="0 0 16 16" aria-hidden="true"><rect x="1" y="3" width="14" height="10" rx="1" fill="#fff"/><path d="M1.5 3.5L8 9l6.5-5.5" fill="none" stroke="#c8202f" stroke-width="1.2"/></svg>
        info@northerncards.com
      </li>
      <li>
        <svg viewBox="0 0 16 16" aria-hidden="true"><circle cx="8" cy="8" r="7" fill="#fff"/><path d="M8 1v14M1 8h14M3 4.5h10M3 11.5h10" stroke="#c8202f" stroke-width="1" fill="none"/><ellipse cx="8" cy="8" rx="3" ry="7" fill="none" stroke="#c8202f" stroke-width="1"/></svg>
        NorthernCards.com
      </li>
    </ul>
  </section>

  <section class="card card--back" aria-label="Business card back">
    <div class="back-pattern" role="img" aria-label="Faint repeated brand-name pattern in darker red"></div>
    <div class="back-logo"><span class="wordmark">Northern Cards</span></div>
    <div class="back-web">NorthernCards.com</div>
  </section>
</body>
</html>
```